Online business manager needs a website

I need a website designed and then coded. I am an online business manager serving a number of different industries providing administrative support to existing small businesses and helping solo practitioners get their new business up and running.

I didn't have a logo formally designed but have been using the attached avatar and wouldn't mind something that incorporated that.

The business doesn't have an official name, so I've just been using my name Lena Pruvost, Online Business Manager or Lena Pruvost, OBM. I've attached two documents that I have made previously for an example of content.

I would prefer the final site be in Wordpress.

Requirements
Must have
• A way to contact me, testimonials, list of services

```html
<!DOCTYPE html>
<html lang="en">
<head>
<meta charset="utf-8">
<title>Lena Pruvost – Online Business Manager</title>
<link href="https://fonts.googleapis.com/css2?family=Roboto:ital,wght@0,400;0,500;0,700;1,400&display=swap" rel="stylesheet">
<style>
:root{
  --purple:#4a1c86;
  --purple-dark:#3a1170;
  --header-bg:#f4effb;
  --ink:#111111;
  --body:#6b6b6b;
  --dark:#4b4b4f;
  --footer:#1c1c20;
  --white:#ffffff;
}
*{margin:0;padding:0;box-sizing:border-box}
html,body{width:1200px;height:3610px;overflow:hidden}
body{font-family:"Roboto",Arial,sans-serif;color:var(--ink);position:relative;background:var(--white)}
.abs{position:absolute}
.btn{position:absolute;display:flex;align-items:center;justify-content:center;background:var(--purple);color:var(--white);font-weight:700;font-size:16px;border-radius:24px;text-decoration:none}

/* header */
.site-header{position:absolute;left:0;top:0;width:1200px;height:127px;background:var(--header-bg)}
.topbar{position:absolute;left:500px;top:0;width:700px;height:42px;background:var(--purple);clip-path:polygon(26px 0,100% 0,100% 100%,0 100%)}
.topbar .item{position:absolute;top:11px;color:var(--white);font-size:14px;font-weight:500;display:flex;align-items:center;gap:8px}
.social{position:absolute;width:28px;height:28px;border:2px solid var(--white);border-radius:50%}
.brand{position:absolute;text-align:center}
.brand .name{font-weight:700;font-size:28px;color:var(--purple)}
.brand .role{font-style:italic;font-size:20px;color:var(--purple)}
.nav a{position:absolute;top:76px;font-size:16px;font-weight:500;color:var(--purple);text-decoration:none;transform:translateX(-50%)}

/* hero */
.hero{position:absolute;left:0;top:127px;width:1200px;height:600px;background:linear-gradient(90deg,#5a3a2b 0%,#8a6a55 30%,#d8d2cc 55%,#b89a7c 75%,#e9e5df 100%)}
.hero-shade{position:absolute;inset:0;background:linear-gradient(90deg,rgba(0,0,0,.45),rgba(0,0,0,0) 55%)}
.hero .welcome{position:absolute;left:113px;top:162px;font-size:25px;font-weight:500;color:var(--white)}
.hero h1{position:absolute;left:113px;top:195px;font-size:50px;line-height:53px;font-weight:700;color:var(--white)}

/* about */
.about-photo{position:absolute;left:228px;top:840px;width:171px;height:189px;background:linear-gradient(180deg,#e8d9c5,#c9a27b 60%,#8f8a86);border-radius:90px 90px 0 0}
.about-name{position:absolute;left:181px;top:1029px;width:266px;height:60px;background:var(--purple);color:var(--white);font-size:34px;font-weight:700;display:flex;align-items:center;justify-content:center}
.about h2{position:absolute;left:600px;top:796px;font-size:36px;font-weight:500}
.about p{position:absolute;left:600px;top:850px;width:430px;font-size:13.4px;line-height:25.7px;color:var(--body)}

/* services */
.services{position:absolute;left:0;top:1176px;width:1200px;height:733px;background:var(--dark)}
.section-title{position:absolute;left:0;width:1200px;text-align:center;font-size:34px;font-weight:700}
.svc{position:absolute;color:var(--white);text-align:center;transform:translateX(-50%)}
.svc h3{font-size:20px;font-weight:700;line-height:29px;margin-bottom:6px}
.svc li{list-style:none;font-size:13.5px;line-height:25.7px;font-weight:500}
.svc li::before{content:"\2713";margin-right:6px;font-weight:700}

/* packages */
.arrow{position:absolute;width:36px;height:36px;border-radius:50%;display:flex;align-items:center;justify-content:center}
.card{position:absolute;top:2054px;width:312px;height:356px;border:2px solid var(--purple);text-align:center}
.card .img{height:212px}
.card .price{margin-top:22px;color:var(--purple);font-size:23px;font-weight:700}
.card .price span{font-size:13px;font-weight:400}
.card p{margin-top:12px;font-size:13.5px;line-height:25.7px;color:var(--body);padding:0 20px}

/* testimonials */
.testimonials{position:absolute;left:0;top:2488px;width:1200px;height:529px;background:linear-gradient(90deg,#3c3a40,#58555a 50%,#3e3c42)}
.quote-mark{position:absolute;font-size:110px;font-weight:700;color:var(--purple);line-height:1;font-family:Georgia,serif}
.testimonials blockquote{position:absolute;left:498px;top:230px;width:570px;font-size:14px;line-height:27.5px;color:var(--white)}

/* contact */
.contact h2{position:absolute;left:109px;top:3082px;font-size:35px;font-weight:700}
.contact p{position:absolute;left:109px;top:3134px;width:720px;font-size:13.5px;line-height:27.5px;color:var(--body)}

/* footer */
.footer{position:absolute;left:0;top:3288px;width:1200px;height:322px;background:var(--footer);color:var(--white)}
.footer h4{position:absolute;font-size:24px;font-weight:500}
.footer .links a{position:absolute;font-size:14px;color:var(--white);text-decoration:none}
.footer .rule{position:absolute;left:111px;top:262px;width:977px;height:1px;background:#777}
.footer .copy{position:absolute;left:0;top:280px;width:1200px;text-align:center;font-size:13px}
</style>
</head>
<body>

<header class="site-header">
  <div class="topbar">
    <span class="social" style="left:38px;top:7px"></span>
    <span class="social" style="left:85px;top:7px"></span>
    <span class="item" style="left:195px">
      <svg width="16" height="18" viewBox="0 0 16 18"><path d="M3 1 L6 1 L7 5 L5 7 Q7 11 10 13 L12 11 L15 12 L15 16 Q8 18 3 11 Q0 6 3 1Z" fill="#fff"/></svg>555.014.2280</span>
    <span class="item" style="left:369px">
      <svg width="24" height="16" viewBox="0 0 24 16"><rect x="1" y="1" width="22" height="14" fill="none" stroke="#fff" stroke-width="2"/><path d="M1 1 L12 9 L23 1" fill="none" stroke="#fff" stroke-width="2"/></svg>hello@lenapruvost-obm.com</span>
  </div>
  <div class="brand" style="left:100px;top:27px;width:240px">
    <div class="name">Lena Pruvost</div>
    <div class="role">Online Business Manager</div>
  </div>
  <nav class="nav">
    <a style="left:418px">About Me</a>
    <a style="left:513px">Services</a>
    <a style="left:628px">Our Packages</a>
    <a style="left:754px">Testimonials</a>
    <a style="left:872px">Contact me</a>
  </nav>
  <a class="btn" style="left:951px;top:64px;width:137px;height:43px">Get Started</a>
</header>

<section class="hero">
  <div role="img" aria-label="Photo of a smiling businesswoman at a meeting desk across from a colleague" style="position:absolute;inset:0"></div>
  <div class="hero-shade"></div>
  <div class="welcome">Welcome&nbsp; To</div>
  <h1>Lena Pruvost<br>Virtual Assistant</h1>
  <a class="btn" style="left:111px;top:335px;width:137px;height:41px">Get Started</a>
</section>

<section class="about">
  <div class="about-photo" role="img" aria-label="Portrait of Lena Pruvost with small work icons around her"></div>
  <div class="about-name">Lena Pruvost</div>
  <h2>About Me</h2>
  <p>Hi! I'm so excited that you have chosen to explore my portfolio. Helping businesses achieve their goals is my passion, and I'm thrilled that with my assistance you will have more time for your own passion project. I thrive while working independently, which means you can be confident when leaving tasks for me. The type of work that lights me up is anything involving organization and/or spreadsheets. You need data analyzed that includes multiple nested if formulas? You have an</p>
  <a class="btn" style="left:600px;top:1055px;width:137px;height:44px">Read More</a>
</section>

<section class="services">
  <h2 class="section-title" style="top:60px;color:var(--white)">Our Services</h2>
  <svg class="abs" style="left:0;top:0" width="1200" height="733" viewBox="0 0 1200 733">
    <g fill="none" stroke="#4a1c86" stroke-width="5" stroke-linecap="round" stroke-dasharray="0.1 11">
      <path d="M106 407 A112 112 0 0 1 330 407"/>
      <path d="M358 407 A112 112 0 0 0 582 407"/>
      <path d="M609 407 A112 112 0 0 1 833 407"/>
      <path d="M860 407 A112 112 0 0 0 1084 407"/>
    </g>
    <g fill="#fff">
      <circle cx="218" cy="407" r="77"/><circle cx="470" cy="407" r="77"/>
      <circle cx="721" cy="407" r="77"/><circle cx="972" cy="407" r="77"/>
    </g>
    <g fill="#4a1c86">
      <rect x="183" y="378" width="72" height="52"/><rect x="178" y="432" width="82" height="6"/>
      <rect x="440" y="375" width="27" height="62"/><rect x="472" y="375" width="28" height="62"/>
      <circle cx="721" cy="407" r="40"/>
      <circle cx="972" cy="395" r="28"/><rect x="942" y="420" width="60" height="16" rx="4"/>
    </g>
    <g fill="#fff">
      <rect x="195" y="390" width="18" height="18" rx="9"/><rect x="475" y="385" width="20" height="4"/><rect x="475" y="398" width="20" height="4"/><rect x="475" y="411" width="20" height="4"/>
      <path d="M448 402 L460 410 L448 418Z"/>
      <rect x="721" y="370" width="3" height="74"/><rect x="684" y="405" width="74" height="3"/>
      <circle cx="972" cy="398" r="10"/>
    </g>
  </svg>
  <div class="svc" style="left:466px;top:140px"><h3>Social Media &amp; Content<br>Management</h3>
    <ul><li>Content Repurposing</li><li>Graphics Creation</li><li>Audiogram Creation</li><li>Search Engine Optimization</li></ul></div>
  <div class="svc" style="left:977px;top:161px"><h3>Business Management</h3>
    <ul><li>Creation of Operating Procedures</li><li>Review of Website Strategy</li><li>Reporting and Analytics</li><li>Project Management</li></ul></div>
  <div class="svc" style="left:216px;top:517px"><h3>Virtual Assistance</h3>
    <ul><li>Calendar Management</li><li>Email Management</li><li>Light Graphic Design</li><li>Data Entry</li></ul></div>
  <div class="svc" style="left:721px;top:520px"><h3>Finance Management</h3>
    <ul><li>Create Invoices</li><li>Track Receivables</li><li>Analyze Expenses</li><li>Year Over Year Analytics</li></ul></div>
</section>

<section class="packages">
  <h2 class="section-title" style="top:1975px">Our Packages</h2>
  <div class="arrow" style="left:30px;top:2219px;background:#8a8a8a">
    <svg width="14" height="14" viewBox="0 0 14 14"><path d="M9 2 L4 7 L9 12" fill="none" stroke="#fff" stroke-width="2.5"/></svg></div>
  <div class="arrow" style="left:1133px;top:2219px;background:var(--purple)">
    <svg width="14" height="14" viewBox="0 0 14 14"><path d="M5 2 L10 7 L5 12" fill="none" stroke="#fff" stroke-width="2.5"/></svg></div>
  <div class="card" style="left:98px">
    <div class="img" role="img" aria-label="Photo of a team working together at laptops" style="background:linear-gradient(135deg,#6e6f72,#c9c5bf 55%,#4c4d52)"></div>
    <div class="price">$40 <span>Hourly Rate</span></div>
    <p>For clients needing only occasional help</p>
  </div>
  <div class="card" style="left:445px">
    <div class="img" role="img" aria-label="Photo of colleagues shaking hands across a meeting table" style="background:linear-gradient(135deg,#8a6f5a,#d9d3cc 50%,#6b5c52)"></div>
    <div class="price">$700 <span>20 hours/month</span></div>
    <p>Includes one 15 minute meeting per week<br>Responses within 72 hours</p>
  </div>
  <div class="card" style="left:792px">
    <div class="img" role="img" aria-label="Photo of a support agent with a headset in an office" style="background:linear-gradient(135deg,#9aa3a8,#e6e6e4 50%,#7c7f85)"></div>
    <div class="price">$1,300 <span>40 hours/month</span></div>
    <p>Includes one 30 minute meeting per week<br>Responses within 48 hours</p>
  </div>
</section>

<section class="testimonials">
  <div role="img" aria-label="Faded office background" style="position:absolute;inset:0"></div>
  <h2 class="section-title" style="top:82px;color:var(--white)">Testimonials</h2>
  <div role="img" aria-label="Portrait photo of the client giving the testimonial" style="position:absolute;left:165px;top:151px;width:294px;height:294px;border-radius:50%;background:radial-gradient(circle at 50% 45%,#c79a7a,#6f7a3e 70%,#4b5a2c)"></div>
  <div class="quote-mark" style="left:480px;top:157px">&ldquo;</div>
  <blockquote>When it became apparent that a project would take more time than I had, Lena stepped up to take on the required research. She was thorough and timely; able to meet a last-minute 12-hour deadline. I would highly recommend Lena to assist with your next project.
    <div style="margin-top:16px;font-weight:700;font-size:15px">Maren T. Holloway,</div>
    <div style="font-size:13.5px;line-height:20px">Brightline Home Services</div>
  </blockquote>
  <div class="quote-mark" style="left:998px;top:360px">&rdquo;</div>
  <div class="arrow" style="left:25px;top:275px;background:#8a8a8a">
    <svg width="14" height="14" viewBox="0 0 14 14"><path d="M9 2 L4 7 L9 12" fill="none" stroke="#fff" stroke-width="2.5"/></svg></div>
  <div class="arrow" style="left:1129px;top:275px;background:var(--white)">
    <svg width="14" height="14" viewBox="0 0 14 14"><path d="M5 2 L10 7 L5 12" fill="none" stroke="#333" stroke-width="2.5"/></svg></div>
</section>

<section class="contact">
  <h2>Contact Me</h2>
  <p>DIGITAL BUSINESS MANAGER focused on the live event and entertainment industry. Helping artists and owners to better manage their career and business by strategically reviewing systems, recommending operational efficiencies, and managing inboxes</p>
  <a class="btn" style="left:935px;top:3099px;width:137px;height:42px">Contact Me</a>
</section>

<footer class="footer">
  <div class="brand" style="left:88px;top:70px;width:260px">
    <div class="name" style="color:var(--white)">Lena Pruvost</div>
    <div class="role" style="color:var(--white)">Online Business Manager</div>
  </div>
  <span class="social" style="left:114px;top:170px;width:32px;height:32px"></span>
  <span class="social" style="left:175px;top:170px;width:32px;height:32px"></span>
  <h4 style="left:375px;top:74px">Navigation</h4>
  <div class="links">
    <a style="left:375px;top:119px">About Me</a>
    <a style="left:375px;top:147px">Our Services</a>
    <a style="left:375px;top:174px">Our Packages</a>
    <a style="left:375px;top:202px">Testimonials</a>
    <a style="left:375px;top:229px">Contact Me</a>
  </div>
  <h4 style="left:591px;top:74px">Contact Me</h4>
  <div class="links">
    <a style="left:591px;top:119px">&#9742;&nbsp;&nbsp; 555.014.2280</a>
    <a style="left:591px;top:147px">&#9993;&nbsp; hello@lenapruvost-obm.com</a>
  </div>
  <h4 style="left:843px;top:74px">Newsletter</h4>
  <div class="abs" style="left:843px;top:128px;width:178px;height:42px;background:#2e2e33;border:1px solid #555;color:#fff;font-size:13.5px;padding:12px 8px">Enter Email Address</div>
  <div class="abs" style="left:1021px;top:128px;width:66px;height:42px;background:var(--purple);display:flex;align-items:center;justify-content:center">
    <svg width="26" height="24" viewBox="0 0 26 24"><path d="M2 11 L24 2 L16 22 L12 13 Z M12 13 L24 2" fill="none" stroke="#fff" stroke-width="1.8" stroke-linejoin="round"/></svg></div>
  <div class="rule"></div>
  <div class="copy">© 2023 Lena Pruvost Virtual Assistant. All rights reserved</div>
</footer>

</body>
</html>
```